Glint5Gate Photography Business Cards

We need a good general business card that we can hand to our clients. We will be doing embossed gloss cards.

Target Market(s)

Real estate / Business to business / professionals

```html
<!DOCTYPE html>
<html lang="en">
<head>
<meta charset="utf-8">
<title>Glint5Gate Photography – Business Cards</title>
<link href="https://fonts.googleapis.com/css2?family=Jost:ital,wght@0,400;0,500;0,600;1,400&display=swap" rel="stylesheet">
<style>
  :root {
    --navy: #29245e;
    --paper: #ffffff;
    --canvas: #ffffff;
    --shadow: rgba(20, 18, 50, 0.28);
  }
  * { margin: 0; padding: 0; box-sizing: border-box; }
  html, body {
    width: 1200px; height: 1200px; overflow: hidden;
    background: var(--canvas);
    font-family: "Jost", "Futura", sans-serif;
    color: var(--navy);
  }
  .stage { position: relative; width: 1200px; height: 1200px; }
  .card {
    position: absolute;
    width: 420px; height: 228px;
    background: var(--paper);
    box-shadow: 0 8px 22px var(--shadow);
    overflow: hidden;
  }
  .card--front { left: 135px; top: 486px; }
  .card--back  { left: 674px; top: 486px; }

  .band { position: absolute; left: 0; width: 100%; height: 11px; background: var(--navy); }
  .band--top { top: 0; }
  .band--bottom { bottom: 0; }

  .holder-name {
    position: absolute; left: 40px; top: 16px;
    font-size: 47px; font-weight: 400; letter-spacing: 4px; line-height: 1;
  }
  .holder-role {
    position: absolute; left: 41px; top: 70px;
    font-size: 17px; font-style: italic; letter-spacing: 1.6px;
  }
  .contact { position: absolute; left: 40px; }
  .contact__label {
    font-size: 14px; font-weight: 500; letter-spacing: 1.4px; line-height: 1;
    padding-bottom: 3px; border-bottom: 1.2px solid var(--navy); width: 94px;
  }
  .contact__value { font-size: 10px; letter-spacing: 1.2px; margin: 5px 0 0 5px; line-height: 1; }
  .contact--phone { top: 116px; }
  .contact--email { top: 160px; }

  .brand {
    position: absolute; left: 0; right: 0; top: 78px;
    text-align: center; font-weight: 600; line-height: 1;
  }
  .brand__name { font-size: 40px; letter-spacing: 0.5px; display: block; }
  .brand__tag { font-size: 17px; letter-spacing: 6px; display: block; margin-top: 6px; }
</style>
</head>
<body>
<main class="stage">
  <section class="card card--front" aria-label="Business card, contact side">
    <h1 class="holder-name">ELIN VARGA</h1>
    <p class="holder-role">Co-Founder</p>
    <div class="contact contact--phone">
      <p class="contact__label">Phone:</p>
      <p class="contact__value">+46 071 84 52 16</p>
    </div>
    <div class="contact contact--email">
      <p class="contact__label">E-mail:</p>
      <p class="contact__value">ElinVarga@glintmail.com</p>
    </div>
    <div class="band band--bottom"></div>
  </section>

  <section class="card card--back" aria-label="Business card, brand side">
    <div class="band band--top"></div>
    <p class="brand">
      <span class="brand__name">Glint5Gate</span>
      <span class="brand__tag">PHOTOGRAPHY</span>
    </p>
    <div class="band band--bottom"></div>
  </section>
</main>
</body>
</html>
```